Mobile App design improvement- Figma

I have four screens need to redesign, and I have the design guide to help you.
The goal is to make the design clean and easy to understand CTA improve UI/UX. You can change the icons, and don't change the fonts or color. Also, if you are doing a great job, I will hire you finish the rest of the design of the app.
Here is our site: https://bellowpine.com
BellowPine App is wishlist:
Hight features and app propositions of the app collaborative shopping and chatting with invited friends and family. Easily to get feedback and make decisions of the products from friends, chat, vote, poll, compare.
Here is the Figma link: https://www.mockboard.example/design/XqTT4LmW82pHd7ZsKe9UvN/BellowPine--App?node-id=31-55102&t=HgRw7NbZp3QeLm5Ky-2
Here is the app links:
IOS app:
https://lnk.example/8QeTp2r

Android app:
https://lnk.example/8QeTp2k
Updates

1. I need to have more design ideas that makes users feel simple and easy to understudy platforms can add products from search products, paste url, and use share button to add proton there wishlist from other e-commerce sites. Simplify the search, paste url, and user share button page, maybe combine search with paste url in the search bar, or switch back and forth with search key, paste URL, or share product from other e-commerce sites. Shop page, maybe show users to pick favorites brands recommended products and popular brands. My profile page, I need to be simple but also give users ability to navigate between the save money and wishlists. Please don’t change my color of the app header and color theme. Tone: Ecommerce marketplace, social media, fun! Highlights invite friends chat, save money, and add product.

Target Market(s)

female CEOs, moms, female interns

Industry/Entity Type

Social networking, shopping.

Number of Pages Required

4 page

Font styles to use
Other font styles liked:
• please look at our brand guide

Requirements
Nice to have
• Simple design, highlight invite memebers, and highlight 3 options for them to get products into one place. Highlight collabrative and social tone.
Should not have
• Don't give me too much colors.

```html
<!DOCTYPE html>
<html lang="en">
<head>
<meta charset="utf-8">
<title>BellowPine App – Screens</title>
<link href="https://fonts.googleapis.com/css2?family=Poppins:wght@400;500;600&family=Tinos:wght@400;700&display=swap" rel="stylesheet">
<style>
:root{
  --brand:#3c3dd0;
  --brand-soft:#ecebff;
  --lime:#a4e52e;
  --teal:#5ee6d3;
  --ink:#1c1c2a;
  --muted:#6b6b7b;
  --line:#e4e4ee;
  --white:#ffffff;
  --star:#f5a623;
  --sans:'Poppins',sans-serif;
  --serif:'Tinos',serif;
}
*{box-sizing:border-box;margin:0;padding:0}
html,body{width:1200px;height:835px;overflow:hidden;background:var(--white)}
body{position:relative;font-family:var(--sans);color:var(--ink)}

.screen{position:absolute;top:44px;width:198px;height:427px;border-radius:26px;overflow:hidden;background:var(--brand)}
.status{position:absolute;top:11px;left:16px;right:16px;display:flex;justify-content:space-between;align-items:center;color:var(--white);font-size:9px;font-weight:500}
.status-icons{display:flex;gap:3px}
.status-icons i{display:block;width:7px;height:5px;background:var(--white);border-radius:1px}
.status-icons i:last-child{width:11px}
.topbar{position:absolute;top:36px;left:14px;right:12px;display:flex;align-items:center;justify-content:space-between;color:var(--white);font-size:10px;line-height:1.2}
.title .back{margin-right:6px}
.title small{display:block;font-size:7px;opacity:.85;padding-left:11px;margin-top:2px}
.avatar-sm{width:19px;height:19px;border-radius:50%;background:linear-gradient(135deg,#d9d3c7,#7d6e5e);border:1.5px solid var(--white);flex:none}
.menu-btn{width:19px;height:19px;border-radius:50%;background:var(--white);display:flex;align-items:center;justify-content:center;flex:none}

.nav{position:absolute;left:0;right:0;bottom:0;height:46px;background:var(--white);display:flex;justify-content:space-around;align-items:flex-start;padding-top:8px;border-top:1px solid var(--line)}
.nav-item{display:flex;flex-direction:column;align-items:center;gap:3px;font-size:5.5px;color:var(--muted)}
.nav-item.active{color:var(--brand);font-weight:500}
.nav-item svg{width:10px;height:10px}

.search-icon{flex:none}

/* profile */
.profile-photo{position:absolute;top:66px;left:14px;width:68px;height:68px;border-radius:50%;border:2px solid #e8c24a;background:linear-gradient(160deg,#e7e2da,#6f7f95)}
.profile-info{position:absolute;top:80px;left:90px;color:var(--white)}
.profile-info .edit{font-size:7px}
.profile-info h1{font-family:var(--serif);font-weight:400;font-size:12.5px;letter-spacing:.3px;margin-top:3px}
.profile-info p{font-family:var(--serif);font-size:7px;margin-top:2px}
.savings{position:absolute;top:148px;left:12px;right:12px;display:grid;grid-template-columns:repeat(3,1fr);gap:6px}
.saving{background:var(--white);border-radius:10px;padding:7px 4px;text-align:center;font-family:var(--serif)}
.saving b{display:block;font-size:13px;color:var(--brand);font-weight:700;line-height:1}
.saving span{display:block;font-size:6.5px;margin-top:4px;color:var(--ink)}
.sheet{position:absolute;left:0;right:0;top:206px;bottom:0;background:var(--white);border-radius:24px 24px 0 0}
.tabs{position:absolute;top:224px;left:14px;right:14px;display:flex;align-items:center;gap:6px;background:#f3f3f8;border-radius:14px;padding:3px}
.tab{flex:1;text-align:center;font-family:var(--serif);font-size:7.5px;padding:5px 0;border-radius:11px;color:var(--muted)}
.tab.active{background:var(--brand);color:var(--white)}
.wish-grid{position:absolute;top:258px;left:14px;right:14px;display:grid;grid-template-columns:1fr 1fr;gap:10px}
.wish-card{height:82px;border-radius:8px;background:linear-gradient(180deg,#78b4bc,#e6d0b8);color:var(--white);padding:5px 6px}
.wish-card b{font-size:6.5px;font-weight:500;display:block}
.wish-card small{font-size:5.5px;display:block;margin-top:3px}
.wish-new{height:82px;border-radius:8px;border:1.5px dashed var(--brand);display:flex;flex-direction:column;align-items:center;justify-content:center;gap:4px;color:var(--brand);font-size:7px;font-weight:500}
.plus-dot{width:20px;height:20px;border-radius:50%;background:var(--brand);color:var(--white);display:flex;align-items:center;justify-content:center;font-size:13px;line-height:1}

/* find products */
.way{position:absolute;left:12px;right:12px;border-radius:20px;padding:11px 14px}
.way .num{display:inline-flex;width:14px;height:14px;border-radius:50%;background:var(--ink);color:var(--white);font-size:7px;align-items:center;justify-content:center;margin-right:5px;vertical-align:2px}
.way h2{font-family:var(--serif);font-weight:400;font-size:11px;line-height:1.25}
.way p{font-size:6px;line-height:1.55;margin-top:5px;color:#3f3f4c}
.way.lime{top:62px;height:104px;background:var(--lime)}
.way.white{top:176px;height:108px;background:var(--white)}
.way.teal{top:294px;height:86px;background:var(--teal)}
.field{margin-top:8px;height:22px;border-radius:11px;background:var(--white);display:flex;align-items:center;gap:6px;padding:0 4px 0 10px;font-size:6px;color:var(--muted)}
.field .go{margin-left:auto;width:16px;height:16px;border-radius:50%;background:var(--brand);display:flex;align-items:center;justify-content:center}
.share-row{margin-top:8px;height:22px;border-radius:11px;background:var(--brand-soft);display:flex;justify-content:space-around;align-items:center}

/* shop */
.shop-panel{position:absolute;top:62px;left:12px;right:12px;height:100px;background:var(--white);border-radius:20px;padding:10px 9px}
.combo{height:26px;border:1.5px solid var(--brand);border-radius:13px;display:flex;align-items:center;gap:6px;padding:0 3px 0 10px;font-size:6.5px;color:var(--muted)}
.seg{margin-left:auto;display:flex;background:#f1f1f7;border-radius:10px;padding:2px}
.seg span{font-size:5.8px;padding:3px 6px;border-radius:8px;color:var(--muted)}
.seg span.on{background:var(--brand);color:var(--white)}
.chips{display:flex;justify-content:center;gap:8px;margin-top:9px}
.chip{font-size:6px;padding:4px 9px;border-radius:10px;border:1px solid var(--line)}
.chip.on{background:var(--lime);border-color:var(--lime)}
.learn{font-size:5px;color:var(--brand);text-decoration:underline;text-align:center;margin-top:8px}
.results{position:absolute;top:170px;left:12px;right:12px;bottom:46px;background:var(--white);border-radius:16px 16px 0 0;padding:9px 6px 0}
.results-head{display:flex;justify-content:space-between;align-items:center;font-size:9.5px;padding:0 6px 6px}
.grid{display:grid;grid-template-columns:1fr 1fr;gap:6px}
.product{border:1px solid var(--line);border-radius:5px;padding:3px;position:relative;height:100px;background:var(--white)}
.product .pic{height:48px;border-radius:3px;background:linear-gradient(135deg,#4b4be0,#3232b8)}
.stars{color:var(--star);font-size:5px;margin-top:3px;letter-spacing:.5px}
.product .name{font-size:5.6px;line-height:1.3;margin-top:1px}
.product .price{font-size:5.6px;margin-top:3px;line-height:1.3}
.product .price b{font-weight:500}
.add{position:absolute;right:4px;bottom:6px;width:13px;height:13px;border-radius:50%;background:var(--brand);color:var(--white);font-size:9px;font-weight:500;display:flex;align-items:center;justify-content:center;line-height:1}

/* wishlist detail */
.screen.long{height:760px;background:var(--white)}
.long .hero{position:absolute;top:0;left:0;right:0;height:160px;background:var(--brand)}
.wish-panel{position:absolute;top:72px;left:12px;right:12px;height:286px;background:var(--white);border-radius:22px;box-shadow:0 3px 12px rgba(0,0,0,.12);padding:6px}
.wish-panel .photo{height:96px;border-radius:17px;background:linear-gradient(135deg,#6a5c6e,#c79a7e 50%,#a9b6c8)}
.fields{padding:0 10px;font-size:6.8px}
.fields p{padding:7px 0;border-bottom:1px solid var(--line)}
.fields p.first{font-weight:500;border:none;padding-top:12px}
.btn{display:flex;align-items:center;justify-content:center;gap:6px;height:30px;margin:12px 6px 0;border-radius:15px;background:var(--brand);color:var(--white);font-size:10px;font-weight:500;box-shadow:0 4px 10px rgba(60,61,208,.35)}
.section{position:absolute;left:12px;right:12px}
.section-head{display:flex;justify-content:space-between;align-items:center}
.section-head h3{font-size:11.5px;font-weight:500}
.links{display:flex;align-items:center;gap:6px;font-size:6.5px;color:var(--brand)}
.pill{background:var(--brand);color:var(--white);border-radius:9px;padding:3px 8px;font-weight:500}
.row{display:flex;justify-content:space-between;margin-top:10px}
.round{width:37px;height:37px;border-radius:50%;flex:none}
.round.invite{border:1.5px dashed var(--brand);display:flex;align-items:center;justify-content:center;color:var(--brand);font-size:16px}
.item{display:flex;flex-direction:column;align-items:center;gap:6px;font-size:5.5px}
.round.ghost{background:var(--white);box-shadow:0 1px 4px rgba(0,0,0,.15)}
.sugg{display:flex;gap:12px;margin-top:8px}
.sugg .product{width:84px;height:114px}
.sugg .pic{height:54px}
.sugg .name,.sugg .price{font-size:6.3px}
</style>
</head>
<body>

<!-- My Profile -->
<section class="screen" style="left:75px">
  <div class="status"><span>9:41</span><span class="status-icons"><i></i><i></i><i></i></span></div>
  <div class="topbar"><span class="title"><span class="back">‹</span>My Profile</span><span class="avatar-sm" role="img" aria-label="User avatar photo"></span></div>
  <div class="profile-photo" role="img" aria-label="Profile portrait photo"></div>
  <div class="profile-info"><span class="edit">Edit ✎</span><h1>MARCUS L</h1><p>@marcusl</p></div>
  <div class="savings">
    <div class="saving"><b>1</b><span>Price Drop</span></div>
    <div class="saving"><b>0</b><span>Coupons</span></div>
    <div class="saving"><b>$</b><span>Earn Cash Back</span></div>
  </div>
  <div class="sheet"></div>
  <div class="tabs"><span class="tab active">My WishLists</span><span class="tab">Joined WishLists</span></div>
  <div class="wish-grid">
    <div class="wish-card" role="img" aria-label="Birthday cake photo"><b>Default WishList 🔒</b><small>● 1 member</small></div>
    <div class="wish-new"><span class="plus-dot">+</span>WishList</div>
  </div>
  <nav class="nav">
    <span class="nav-item active"><svg viewBox="0 0 10 10"><path d="M1 5 5 1.5 9 5V9H1Z" fill="currentColor"/></svg>Home</span>
    <span class="nav-item"><svg viewBox="0 0 10 10"><circle cx="5" cy="5" r="4" fill="none" stroke="currentColor"/></svg>Discover</span>
    <span class="nav-item"><svg viewBox="0 0 10 10"><rect x="1" y="1" width="8" height="8" rx="2" fill="none" stroke="currentColor"/><path d="M5 3v4M3 5h4" stroke="currentColor"/></svg>WishList</span>
    <span class="nav-item"><svg viewBox="0 0 10 10"><path d="M1 5a4 3.5 0 1 1 2 3L1 9Z" fill="none" stroke="currentColor"/></svg>Chat</span>
    <span class="nav-item"><svg viewBox="0 0 10 10"><path d="M1 2h1.5l1 5h5l1-4H3" fill="none" stroke="currentColor"/></svg>Shop</span>
  </nav>
</section>

<!-- 3 Ways to Find Products -->
<section class="screen" style="left:346px">
  <div class="status"><span>9:41</span><span class="status-icons"><i></i><i></i><i></i></span></div>
  <div class="topbar"><span class="title"><span class="back">‹</span>3 Ways to Find Products</span><span class="avatar-sm" role="img" aria-label="User avatar photo"></span></div>
  <div class="way lime">
    <h2><span class="num">1</span>Search for Products</h2>
    <p>Find products the traditional<br>way with the Search bar</p>
    <div class="field"><svg class="search-icon" width="9" height="9" viewBox="0 0 10 10"><circle cx="4" cy="4" r="3" fill="none" stroke="#3c3dd0" stroke-width="1.5"/><path d="M6.5 6.5 9 9" stroke="#3c3dd0" stroke-width="1.5"/></svg>Find what you're looking for<span class="go"><svg width="7" height="7" viewBox="0 0 10 10"><path d="M2 5h6M5.5 2.5 8 5 5.5 7.5" fill="none" stroke="#fff" stroke-width="1.6"/></svg></span></div>
  </div>
  <div class="way white">
    <h2><span class="num">2</span>Save Products from App<br>or Website</h2>
    <p>Use the Share button on other retailer sites or apps to save items to your BellowPine Wishlist</p>
    <div class="share-row">
      <svg width="9" height="9" viewBox="0 0 10 10"><path d="M5 7V1M2.5 3.5 5 1l2.5 2.5M1.5 9h7" fill="none" stroke="#3c3dd0"/></svg>
      <svg width="9" height="9" viewBox="0 0 10 10"><rect x="2" y="4" width="6" height="5" rx="1" fill="none" stroke="#3c3dd0"/><path d="M5 6V1M3.5 2.5 5 1l1.5 1.5" fill="none" stroke="#3c3dd0"/></svg>
      <svg width="9" height="9" viewBox="0 0 10 10"><circle cx="2" cy="5" r="1.3" fill="#3c3dd0"/><circle cx="8" cy="2" r="1.3" fill="#3c3dd0"/><circle cx="8" cy="8" r="1.3" fill="#3c3dd0"/><path d="M2 5 8 2M2 5l6 3" stroke="#3c3dd0"/></svg>
      <svg width="9" height="9" viewBox="0 0 10 10"><circle cx="5" cy="2" r="1" fill="#3c3dd0"/><circle cx="5" cy="5" r="1" fill="#3c3dd0"/><circle cx="5" cy="8" r="1" fill="#3c3dd0"/></svg>
      <svg width="9" height="9" viewBox="0 0 10 10"><path d="M1 8c1-3 3-4 6-4M5.5 1.5 8 4 5.5 6.5" fill="none" stroke="#3c3dd0"/></svg>
    </div>
  </div>
  <div class="way teal">
    <h2><span class="num">3</span>Find Product by URL</h2>
    <p>Visit your favorite stores online and<br>copy and paste the product URL</p>
    <div class="field"><svg class="search-icon" width="9" height="9" viewBox="0 0 10 10"><circle cx="4" cy="4" r="3" fill="none" stroke="#3c3dd0" stroke-width="1.5"/><path d="M6.5 6.5 9 9" stroke="#3c3dd0" stroke-width="1.5"/></svg>Paste Product URL<span class="go"><svg width="7" height="7" viewBox="0 0 10 10"><path d="M2 5h6M5.5 2.5 8 5 5.5 7.5" fill="none" stroke="#fff" stroke-width="1.6"/></svg></span></div>
  </div>
  <nav class="nav">
    <span class="nav-item active"><svg viewBox="0 0 10 10"><path d="M1 5 5 1.5 9 5V9H1Z" fill="currentColor"/></svg>Home</span>
    <span class="nav-item"><svg viewBox="0 0 10 10"><circle cx="5" cy="5" r="4" fill="none" stroke="currentColor"/></svg>Discover</span>
    <span class="nav-item"><svg viewBox="0 0 10 10"><rect x="1" y="1" width="8" height="8" rx="2" fill="none" stroke="currentColor"/><path d="M5 3v4M3 5h4" stroke="currentColor"/></svg>WishList</span>
    <span class="nav-item"><svg viewBox="0 0 10 10"><path d="M1 5a4 3.5 0 1 1 2 3L1 9Z" fill="none" stroke="currentColor"/></svg>Chat</span>
    <span class="nav-item"><svg viewBox="0 0 10 10"><path d="M1 2h1.5l1 5h5l1-4H3" fill="none" stroke="currentColor"/></svg>Shop</span>
  </nav>
</section>

<!-- Shop -->
<section class="screen" style="left:608px">
  <div class="status"><span>9:41</span><span class="status-icons"><i></i><i></i><i></i></span></div>
  <div class="topbar"><span class="title"><span class="back">‹</span>Shop</span><span class="menu-btn"><svg width="8" height="6" viewBox="0 0 8 6"><path d="M0 .5h8M0 3h8M0 5.5h8" stroke="#1c1c2a"/></svg></span></div>
  <div class="shop-panel">
    <div class="combo"><svg class="search-icon" width="9" height="9" viewBox="0 0 10 10"><circle cx="4" cy="4" r="3" fill="none" stroke="#3c3dd0" stroke-width="1.5"/><path d="M6.5 6.5 9 9" stroke="#3c3dd0" stroke-width="1.5"/></svg>Search<span class="seg"><span class="on">Search</span><span>Paste URL</span></span></div>
    <div class="chips"><span class="chip on">Favorite Brands</span></div>
    <div class="learn">Learn more: 3 Ways to Save Products</div>
  </div>
  <div class="results">
    <div class="results-head"><span>Search Results</span><svg width="9" height="7" viewBox="0 0 9 7"><path d="M0 .5h9M0 3.5h9M0 6.5h9" stroke="#1c1c2a"/></svg></div>
    <div class="grid">
      <div class="product"><div class="pic" role="img" aria-label="Black high top sneaker photo"></div><div class="stars">★★★★☆</div><div class="name">Stride High Top Mens Fashion Sneakers</div><div class="price"><b>Now $109</b><br>$129.99</div><span class="add">+</span></div>
      <div class="product"><div class="pic" role="img" aria-label="Black high top sneaker photo"></div><div class="stars">★★★★☆</div><div class="name">Stride High Top Mens Fashion Sneakers</div><div class="price"><b>Now $109</b><br>$129.99</div><span class="add">+</span></div>
      <div class="product"><div class="pic" role="img" aria-label="Black high top sneaker photo"></div><div class="stars">★★★★☆</div><div class="name">Stride High Top Mens Fashion Sneakers</div><div class="price"><b>Now $109</b><br>$129.99</div><span class="add">+</span></div>
      <div class="product"><div class="pic" role="img" aria-label="Black high top sneaker photo"></div><div class="stars">★★★★☆</div><div class="name">Stride High Top Mens Fashion Sneakers</div><div class="price"><b>Now $109</b><br>$129.99</div><span class="add">+</span></div>
    </div>
  </div>
  <nav class="nav">
    <span class="nav-item"><svg viewBox="0 0 10 10"><path d="M1 5 5 1.5 9 5V9H1Z" fill="currentColor"/></svg>Home</span>
    <span class="nav-item"><svg viewBox="0 0 10 10"><circle cx="5" cy="5" r="4" fill="none" stroke="currentColor"/></svg>Discover</span>
    <span class="nav-item"><svg viewBox="0 0 10 10"><rect x="1" y="1" width="8" height="8" rx="2" fill="none" stroke="currentColor"/><path d="M5 3v4M3 5h4" stroke="currentColor"/></svg>WishList</span>
    <span class="nav-item"><svg viewBox="0 0 10 10"><path d="M1 5a4 3.5 0 1 1 2 3L1 9Z" fill="none" stroke="currentColor"/></svg>Chat</span>
    <span class="nav-item active"><svg viewBox="0 0 10 10"><path d="M1 2h1.5l1 5h5l1-4H3" fill="none" stroke="currentColor"/></svg>Shop</span>
  </nav>
</section>

<!-- Default Wishlist -->
<section class="screen long" style="left:886px;width:200px">
  <div class="hero"></div>
  <div class="status"><span>9:41</span><span class="status-icons"><i></i><i></i><i></i></span></div>
  <div class="topbar"><span class="title"><span class="back">‹</span>Default Wishlist<small>@marcusl</small></span><span class="avatar-sm" role="img" aria-label="User avatar photo"></span></div>
  <div class="wish-panel">
    <div class="photo" role="img" aria-label="Group of friends celebrating at a party"></div>
    <div class="fields">
      <p class="first">Add Description of Your Wishlist:</p>
      <p>Title :</p>
      <p>Date :</p>
      <p>Address :</p>
      <p>Details of the event or requirements</p>
    </div>
    <span class="btn"><svg width="10" height="10" viewBox="0 0 10 10"><path d="M1 5a4 3.5 0 1 1 2 3L1 9Z" fill="none" stroke="#fff"/></svg>Open Chat</span>
  </div>
  <div class="section" style="top:376px">
    <div class="section-head"><h3>Members</h3><span class="links"><span class="pill">+ Add</span>View All</span></div>
    <div class="row">
      <span class="round" role="img" aria-label="Member photo" style="background:linear-gradient(135deg,#3aa37a,#c8784a)"></span>
      <span class="round" role="img" aria-label="Member photo" style="background:linear-gradient(135deg,#7a5a3a,#d7b08a)"></span>
      <span class="round" role="img" aria-label="Member photo" style="background:linear-gradient(135deg,#5a4a42,#a58a76)"></span>
      <span class="round invite">+</span>
    </div>
  </div>
  <div class="section" style="top:468px">
    <div class="section-head"><h3>Products</h3><span class="links"><span class="pill">+ Add</span>View All</span></div>
    <div class="row">
      <span class="item"><span class="round" style="background:var(--brand)"></span>xxxx</span>
      <span class="item"><span class="round ghost" role="img" aria-label="Plush toy product photo" style="background:radial-gradient(circle,#8f8fe0 30%,#fff 32%)"></span>xxxx</span>
      <span class="item"><span class="round ghost"></span>xxxx</span>
      <span class="item"><span class="round ghost"></span>xxxx</span>
    </div>
  </div>
  <div class="section" style="top:566px">
    <div class="section-head"><h3>Suggested Products</h3></div>
    <div class="sugg">
      <div class="product"><div class="pic" role="img" aria-label="Black high top sneaker photo"></div><div class="stars">★★★★☆</div><div class="name">Stride High Top Mens Fashion Sneakers</div><div class="price"><b>Now $109</b><br>$129.99</div><span class="add">+</span></div>
      <div class="product"><div class="pic" role="img" aria-label="Black high top sneaker photo"></div><div class="stars">★★★★☆</div><div class="name">Stride High Top Mens Fashion Sneakers</div><div class="price"><b>Now $109</b><br>$129.99</div><span class="add">+</span></div>
    </div>
  </div>
  <nav class="nav">
    <span class="nav-item"><svg viewBox="0 0 10 10"><path d="M1 5 5 1.5 9 5V9H1Z" fill="currentColor"/></svg>Home</span>
    <span class="nav-item"><svg viewBox="0 0 10 10"><circle cx="5" cy="5" r="4" fill="none" stroke="currentColor"/></svg>Discover</span>
    <span class="nav-item active"><svg viewBox="0 0 10 10"><rect x="1" y="1" width="8" height="8" rx="2" fill="none" stroke="currentColor"/><path d="M5 3v4M3 5h4" stroke="currentColor"/></svg>WishList</span>
    <span class="nav-item"><svg viewBox="0 0 10 10"><path d="M1 5a4 3.5 0 1 1 2 3L1 9Z" fill="none" stroke="currentColor"/></svg>Chat</span>
    <span class="nav-item"><svg viewBox="0 0 10 10"><path d="M1 2h1.5l1 5h5l1-4H3" fill="none" stroke="currentColor"/></svg>Shop</span>
  </nav>
</section>

</body>
</html>
```